TRAVEX CONSULTING / PROJECT MANAGEMENT WEB DESIGN

Design Brief: Travex Consulting Website

I own 'TRAVEX' business name and therefore can keep the name and logo simple i.e. TRAVEX only and incorporate consulting / Project Management within the design or text.

Purpose:

The purpose of this project is to create a website for Travex.com.au, a project management consulting company. The website will promote the company's services, allowing potential clients to learn more about Travex and its capabilities. The website should be professional, easy to navigate, and provide all necessary information for potential clients.

Target Audience:

Clients in the Oil & Gas, LNG, and Chemical industry
Businesses and organizations in need of project management and engineering consultancy services
Potential clients looking for information about the company and its services
Key Elements:
Clean and modern design that reflects the company's professional image and incorporates the company logo

Clear and easy-to-use navigation menu

“Homepage” that promotes the company's main services and includes the company's mission statement.

Services:

PROJECT MANAGEMENT
PROJECT ENGINEERING
QUALITY MANAGEMENT AND PROCESS DEVELOPMENT
BUSINESS CASE DEVELOPMENT
ENGINEERING & DESIGN MANAGEMENT
CONCEPT STUDIES AND PROJECT SUPPORT
CONSTRUCTION MANAGEMENT
CONTRACT MANAGEMENT / CLAIMS PROCUREMENT / SUPPLY CHAIN SUPPORT
COMMERCIAL LIABILITY & RISK MANAGEMENT

Mission Statement:

"Our mission at Travex is to provide expert project management and engineering consultancy services that help our clients achieve their goals and exceed their expectations. We will accomplish this by offering a full range of services, providing experienced and highly-qualified professionals, building strong relationships with our clients, continuously improving our services, and maintaining a reputation for excellence."

"About" page that includes client-supplied text about the company
"Contact" page with an editable form, email, and phone number for potential clients to get in touch with the company

Design Style:

Professional and modern
Clean and simple layout
Use of the company's colors and branding (subject to change)
Use of high-quality images that reflect the industry and services

Functionality:
Responsive design that is optimized for all devices and screen sizes

Website will be coded and uploaded to a content management system (CMS) for easy updates and maintenance
Website will be optimized for search engines and include all necessary SEO elements
Website will be fully tested for compatibility with all modern web browsers and devices
Website will be secured with an SSL certificate to ensure the safety of user data (client hosting includes SSL certificate).

Target Market(s)

Clients in the Oil & Gas, LNG, and Chemical industry Businesses and organizations in need of project management and engineering consultancy services Potential clients looking for information about the company and its services

Industry/Entity Type

Oil & Gas, LNG, and Chemical industry Businesses and organizations

Coding

Coded - Design and coding required

Number of Pages Required

3 page

Font styles to use
Sans Serif

Colors
0054AA
0677BA
7BADD7
CADEEF
E8F1F8
EB3D1F
EC4F4E
F09395
F8D3D4
FCEDEE
6B429C
8869AF
B7A5CE
E3DAEB
F3F0F8

Requirements
Must have
• HOME ABOUT AND CONTACT PAGE
Nice to have
• Fresh look, open to ideas
Should not have
• Stock images and hand shakes and meeting rooms..

```html
<!DOCTYPE html>
<html lang="en">
<head>
<meta charset="utf-8">
<title>Travex Consulting — Project Management and Engineering Consultancy</title>
<link href="https://fonts.googleapis.com/css2?family=Bebas+Neue&family=Poppins:wght@400;500;600;700&display=swap" rel="stylesheet">
<style>
:root{
  --blue:#2a9df4;
  --blue-deep:#0054aa;
  --ink:#1d2330;
  --text:#4a4f5a;
  --muted:#8a8f99;
  --pale:#eef2f7;
  --white:#ffffff;
  --dark:#1a1c21;
  --dark-2:#23262c;
  --line:#3a3e46;
}
*{margin:0;padding:0;box-sizing:border-box}
html,body{width:1200px;height:4005px;overflow:hidden}
body{position:relative;background:var(--white);font-family:"Poppins",sans-serif;color:var(--text)}
.abs{position:absolute}
.display{font-family:"Bebas Neue",sans-serif;font-weight:400;letter-spacing:.5px;color:var(--ink);line-height:1}
.bar-title{padding-left:10px;border-left:3px solid var(--blue)}
.btn{position:absolute;background:var(--blue);color:var(--white);font-family:"Bebas Neue",sans-serif;font-size:15px;letter-spacing:1px;display:flex;align-items:center;justify-content:center;border-radius:2px}
.photo{position:absolute}

/* header */
.site-header{left:0;top:0;width:1200px;height:75px;background:var(--white);z-index:3}
.brand-badge{left:155px;top:-14px;width:110px;height:110px;border-radius:50%;background:var(--white);display:flex;align-items:center;justify-content:center;z-index:4}
.brand-name{font-family:"Poppins",sans-serif;font-weight:700;font-size:20px;color:var(--blue);letter-spacing:1px}
.nav a{position:absolute;top:28px;font-size:11.5px;color:var(--ink);text-decoration:none}
.nav a.active{color:var(--blue)}
.header-phone{left:1013px;top:0;width:187px;height:75px;background:var(--blue);color:var(--white)}
.header-phone small{position:absolute;left:33px;top:17px;font-size:10px}
.header-phone strong{position:absolute;left:33px;top:32px;font-family:"Bebas Neue",sans-serif;font-size:24px;font-weight:400;letter-spacing:.5px}
.header-phone svg{position:absolute;left:-6px;top:22px}

/* hero */
.hero{left:0;top:75px;width:1200px;height:550px;background:linear-gradient(180deg,#5a7ea6 0%,#7d92a8 35%,#3e4f63 65%,#1c2735 100%)}
.hero-title{left:157px;top:432px;border-left:3px solid var(--blue);padding-left:10px;font-family:"Bebas Neue",sans-serif;font-size:40px;line-height:.98;color:var(--white)}
.hero-title span{color:var(--blue)}
.hero-lead{left:169px;top:524px;width:470px;font-size:12.5px;line-height:21px;color:var(--white)}
.play-ring{left:845px;top:393px;width:186px;height:186px;border-radius:50%;background:rgba(255,255,255,.08)}
.play-btn{left:909px;top:457px;width:56px;height:56px;border-radius:50%;border:2px solid var(--white)}

/* about */
.about{left:0;top:625px;width:1200px;height:634px;background:var(--pale)}
.about-photo-main{left:225px;top:710px;width:350px;height:418px;background:linear-gradient(135deg,#7a8fa0,#3f6c86 55%,#c49a52)}
.about-photo-small{left:169px;top:1005px;width:201px;height:193px;background:linear-gradient(160deg,#8b6c4e,#c8d34f 60%,#54606b);border:3px solid var(--white)}
.mark-circle{width:88px;height:88px;border-radius:50%;background:var(--white);box-shadow:0 4px 16px rgba(0,0,0,.12);display:flex;align-items:center;justify-content:center}
.mark-circle span{width:58px;height:58px;border-radius:50%;border:3px solid var(--blue)}
.about-title{left:615px;top:718px;font-size:32px}
.about-copy{left:625px;top:776px;width:390px;font-size:11.5px;line-height:22.5px}
.about-copy p+p{margin-top:22px}
.contact-inline{left:839px;top:1074px}
.contact-inline small{position:absolute;left:42px;top:0;font-size:9px;white-space:nowrap;color:var(--ink)}
.contact-inline strong{position:absolute;left:42px;top:14px;font-family:"Bebas Neue",sans-serif;font-size:21px;font-weight:400;color:var(--blue);white-space:nowrap}

/* services */
.services-title{left:513px;top:1339px;font-size:32px}
.service-grid{left:0;top:1411px;width:1200px;height:841px;display:grid;grid-template-columns:repeat(3,400px);grid-template-rows:repeat(3,280.3px)}
.service-tile{position:relative;display:flex;align-items:flex-end;padding:0 31px 26px}
.service-tile h3{font-family:"Bebas Neue",sans-serif;font-weight:400;font-size:24px;line-height:1;color:var(--white);position:relative}
.service-tile::after{content:"";position:absolute;inset:0;background:linear-gradient(180deg,rgba(0,0,0,0) 45%,rgba(0,0,0,.45))}
.service-tile h3{z-index:1}
.t1{background:linear-gradient(135deg,#c9b9a6,#6d6a68 60%,#2a3240)}
.t2{background:linear-gradient(135deg,#d9dde2,#9fb4c8 55%,#2a9df4)}
.t3{background:linear-gradient(135deg,#8aa3b6,#5d7080 50%,#3b3f45)}
.t4{background:linear-gradient(135deg,#7b8590,#4b5058 55%,#2b2f36)}
.t5{background:linear-gradient(135deg,#c8c3bb,#8c8882 55%,#3e3f42)}
.t6{background:linear-gradient(135deg,#d3d6da,#8a8d92 55%,#3a3c40)}
.t7{background:linear-gradient(135deg,#5b6d7d,#8b8a5a 50%,#2f3338)}
.t8{background:linear-gradient(135deg,#2b3e4a,#4e6a78 50%,#1b252d)}
.t9{background:linear-gradient(135deg,#7a5a44,#a07654 50%,#3a2a22)}

/* mission */
.mission-photo{left:592px;top:2342px;width:608px;height:438px;background:linear-gradient(135deg,#1e3a64,#2f6aa8 45%,#152238)}
.mission-title{left:162px;top:2418px;font-size:32px}
.mission-copy{left:171px;top:2470px;width:350px;font-size:11px;line-height:20px}
.mission-copy p+p{margin-top:20px}

/* quote */
.quote{left:0;top:2860px;width:1200px;height:650px;background:linear-gradient(180deg,#ffffff,#f3f4f6)}
.eyebrow{left:0;top:2944px;width:1200px;text-align:center;font-family:"Bebas Neue",sans-serif;font-size:13px;color:var(--blue);letter-spacing:.5px}
.quote-title{left:0;top:2968px;width:1200px;text-align:center;font-size:32px}
.quote-lead{left:360px;top:3006px;width:480px;text-align:center;font-size:11.5px;line-height:21px}
.field{position:absolute;background:var(--white);border:1px solid #e6e8ec;font-size:10.5px;color:var(--muted);padding:14px 19px}
.caret{position:absolute;right:14px;top:18px;width:0;height:0;border-left:5px solid transparent;border-right:5px solid transparent;border-top:5px solid var(--ink)}

/* footer */
.footer{left:0;top:3510px;width:1200px;height:495px;background:var(--dark)}
.footer-brand{left:186px;top:3560px;font-size:22px}
.cta-title{left:521px;top:3556px;font-size:32px;color:var(--white)}
.cta-rule{height:2px;background:var(--blue);top:3633px}
.footer-panel{left:169px;top:3670px;width:1031px;height:335px;background:var(--dark-2)}
.fcol{position:absolute;top:3714px}
.fcol h4{font-family:"Bebas Neue",sans-serif;font-weight:400;font-size:15px;color:var(--white);letter-spacing:.5px;border-top:1px solid var(--line);padding-top:16px;margin-bottom:14px}
.fcol ul{list-style:none}
.fcol li{font-size:9.5px;color:#9a9ea6;line-height:13px;margin-bottom:13.4px}
.footer-base{left:218px;top:3970px;width:745px;border-top:1px solid var(--line);padding-top:12px;font-size:9px;color:#80848c;display:flex;justify-content:space-between}
.footer-base a{color:var(--blue);text-decoration:none}
</style>
</head>
<body>

<header class="abs site-header">
  <nav class="nav">
    <a class="active" style="left:519px" href="#">Home</a>
    <a style="left:592px" href="#">About</a>
    <a style="left:667px" href="#">Services</a>
    <a style="left:752px" href="#">Mission Statement</a>
    <a style="left:892px" href="#">Contact Us</a>
  </nav>
  <div class="abs header-phone">
    <svg width="30" height="30" viewBox="0 0 24 24" fill="none" stroke="#fff" stroke-width="1.6"><path d="M6.6 3.5l2.6 3.2-1.6 2.2c1 2.2 2.9 4.2 5.2 5.3l2.2-1.6 3.2 2.6-1.6 3c-6.8-.4-12.4-6-12.8-12.8z"/></svg>
    <small>Contact Us Today</small>
    <strong>010-555-246-810</strong>
  </div>
</header>
<div class="abs brand-badge"><span class="brand-name">TRAVEX</span></div>

<section class="abs hero" role="img" aria-label="Industrial storage silos under a cloudy sky"></section>
<h1 class="abs hero-title">Project Management<br>and Engineering <span>Consultancy</span></h1>
<p class="abs hero-lead">Lorem ipsum dolor sit amet, consectetur adipisicing elit, sed do eiusmod tempor incididunt ut labore et dolore magna aliqua. Ut enim.</p>
<div class="abs play-ring"></div>
<div class="abs play-btn"><svg width="52" height="52" viewBox="0 0 52 52"><path d="M23 21l8 5-8 5z" fill="#fff"/></svg></div>

<section class="abs about"></section>
<div class="photo about-photo-main" role="img" aria-label="Team of consultants greeting a client"></div>
<div class="photo about-photo-small" role="img" aria-label="Site engineer in hard hat holding a clipboard"></div>
<div class="abs mark-circle" style="left:183px;top:750px"><span></span></div>
<h2 class="abs display bar-title about-title">About Travex Consulting</h2>
<div class="abs about-copy">
  <p>Lorem ipsum dolor sit amet, consectetur adipisicing elit, sed do eiusmod tempor incididunt ut labore et dolore magna aliqua. Ut enim ad minim veniam, quis nostrud exercitation ullamco laboris nisi ut aliquip ex ea commodo consequat.</p>
  <p>Duis aute irure dolor in reprehenderit in voluptate velit esse cillum dolore eu fugiat nulla pariatur. Excepteur sint occaecat cupidatat non proident, sunt in culpa qui officia deserunt mollit anim id est laborum. Sed ut perspiciatis unde omnis iste natus error sit voluptatem antium doloremque laudantium, totam rem aperiam, eaque ipsa quae ab illo inventore veritatis et quasi architecto beatae vitae dicta sunt, explicabo. Nemo enim ipsam.</p>
</div>
<a class="btn" style="left:625px;top:1074px;width:180px;height:39px" href="#">Read More About Us</a>
<div class="abs contact-inline">
  <svg width="34" height="34" viewBox="0 0 24 24" fill="none" stroke="#1d2330" stroke-width="1.2"><circle cx="12" cy="12" r="11"/><path d="M7.5 5.5l2 2.5-1.2 1.6c.8 1.7 2.2 3.2 4 4l1.6-1.2 2.5 2-1.2 2.3c-5.2-.3-9.5-4.6-9.8-9.8z"/></svg>
  <small>Contact Us Today</small>
  <strong>010-555-246-810</strong>
</div>

<h2 class="abs display bar-title services-title">Our Services</h2>
<div class="abs service-grid">
  <div class="service-tile t1" role="img" aria-label="Consultant reviewing a project board"><h3>Project Management</h3></div>
  <div class="service-tile t2" role="img" aria-label="Engineer drafting plans beside a hard hat"><h3>Project Engineering</h3></div>
  <div class="service-tile t3" role="img" aria-label="Quality manager with tablet in a warehouse"><h3>Quality Management and<br>Process Development</h3></div>
  <div class="service-tile t4" role="img" aria-label="Hand with pen pointing at charts on a tablet"><h3>Business Case Development</h3></div>
  <div class="service-tile t5" role="img" aria-label="Hand sketching engineering drawings"><h3>Engineering &amp; Design Management</h3></div>
  <div class="service-tile t6" role="img" aria-label="Team working together on concept studies"><h3>Concept Studies and<br>Project Support</h3></div>
  <div class="service-tile t7" role="img" aria-label="Construction workers in hard hats over site plans"><h3>Construction Management</h3></div>
  <div class="service-tile t8" role="img" aria-label="Technician working in a server room"><h3>Supply Chain Support</h3></div>
  <div class="service-tile t9" role="img" aria-label="Hand stopping falling wooden blocks"><h3>Commercial Liability &amp;<br>Risk Management</h3></div>
</div>

<div class="photo mission-photo" role="img" aria-label="Operators monitoring screens in a control room"></div>
<div class="abs mark-circle" style="left:548px;top:2517px"><span></span></div>
<h2 class="abs display bar-title mission-title">Mission Statement</h2>
<div class="abs mission-copy">
  <p>"Our mission at Travex is to provide expert project management and engineering consultancy services that help our clients achieve their goals and exceed their expectations.</p>
  <p>We will accomplish this by offering a full range of services, providing experienced and highly-qualified professionals, building strong relationships with our clients, continuously improving our services, and maintaining a reputation for excellence."</p>
</div>
<a class="btn" style="left:171px;top:2656px;width:137px;height:37px" href="#">Get Started</a>

<section class="abs quote"></section>
<p class="abs eyebrow">Get In Touch</p>
<h2 class="abs display quote-title">Request a Quote</h2>
<p class="abs quote-lead">Contact us today to see how our creative international courier solutions can get your expedited shipments delivered on time and in perfect condition.</p>
<form>
  <div class="field" style="left:277px;top:3086px;width:322px;height:41px">Full Name*</div>
  <div class="field" style="left:605px;top:3086px;width:323px;height:41px">Last Name*</div>
  <div class="field" style="left:277px;top:3136px;width:322px;height:41px">Company*</div>
  <div class="field" style="left:605px;top:3136px;width:323px;height:41px">Business Email*</div>
  <div class="field" style="left:277px;top:3187px;width:322px;height:41px">Phone Number*</div>
  <div class="field" style="left:605px;top:3187px;width:323px;height:41px">What do you need?<span class="caret"></span></div>
  <div class="field" style="left:277px;top:3239px;width:651px;height:121px">How Can We Help?</div>
  <a class="btn" style="left:516px;top:3392px;width:168px;height:38px" href="#">Request a Quote</a>
</form>

<footer class="abs footer"></footer>
<div class="abs footer-brand brand-name">TRAVEX</div>
<h2 class="abs display cta-title">Connect with a Travex Consulting<br>Businesses Expert Today</h2>
<svg class="abs" style="left:976px;top:3574px" width="40" height="28" viewBox="0 0 40 28" fill="none" stroke="#fff" stroke-width="3"><path d="M2 14h34M24 3l12 11-12 11"/></svg>
<div class="abs cta-rule" style="left:521px;width:438px"></div>
<div class="abs cta-rule" style="left:967px;width:65px"></div>
<div class="abs footer-panel"></div>

<div class="fcol" style="left:222px;width:150px">
  <h4>Company</h4>
  <ul><li>Home</li><li>About</li><li>Services</li><li>Mission Statement</li><li>Contact Us</li></ul>
</div>
<div class="fcol" style="left:423px;width:150px">
  <h4>Services</h4>
  <ul><li>Project Management</li><li>Project Engineering</li><li>Quality Management And<br>Process Development</li><li>Business Case Development</li><li>Engineering &amp; Design Management</li></ul>
</div>
<div class="fcol" style="left:637px;width:220px">
  <h4 style="border-top-color:transparent;color:transparent">Services</h4>
  <ul><li>Concept Studies And Project Support</li><li>Construction Management</li><li>Contract Management / Claims Procurement<br>/ Supply Chain Support</li><li>Commercial Liability &amp; Risk Management</li></ul>
</div>
<div class="fcol" style="left:876px;width:150px">
  <h4>Solutions</h4>
  <ul><li>Lorem ipsum dolor</li><li>Lorem ipsum dolor</li><li>Lorem ipsum dolor</li><li>Lorem ipsum dolor</li><li>Lorem ipsum dolor</li><li>Lorem ipsum dolor</li></ul>
</div>
<div class="abs footer-base">
  <span>Copyright © 2023 <a href="#">Travex Consulting</a>. All Rights Reserved.</span>
  <span>Terms of Use &amp; Privacy Policy</span>
</div>

</body>
</html>
```